Design a Mobile App for Landscape Businesses

This project is to design the first three screens for a mobile app for Landscape and Lawncare businesses. This app will serve as a directory for homeowners to locate landscape and lawn care businesses and for landscape businesses and contractors to run their business. See the attached PDF for more information and example
Here is the link to the description https://brevlinq.test/k3r92P

Target Market(s)

Landscape and lawn care business, gardeners, home owners

Industry/Entity Type

Landscape Gardening

Logo Text

Quillmoray

Colors

Designer to choose colors to be used in the design.

```html
<!DOCTYPE html>
<html lang="en">
<head>
<meta charset="utf-8">
<title>Quillmoray – Add/Edit Business</title>
<link href="https://fonts.googleapis.com/css2?family=Montserrat:wght@300;400;500;600&display=swap" rel="stylesheet">
<style>
  :root {
    --page-bg: #f0f0f0;
    --screen-bg: #e6e6e6;
    --brand-green: #2bc28a;
    --field-bg: #ffffff;
    --placeholder: #c4c4c4;
    --text-dark: #1e1e1e;
    --label-grey: #777777;
    --arrow-grey: #8a8a8a;
  }
  * { box-sizing: border-box; margin: 0; padding: 0; }
  html, body {
    width: 1200px; height: 1200px; overflow: hidden;
    background: var(--page-bg);
    font-family: "Montserrat", sans-serif;
  }
  .app-screen {
    position: absolute; left: 268px; top: 12px;
    width: 663px; height: 1175px;
    background: var(--screen-bg);
    border: 1px solid #2a2a2a;
    overflow: hidden;
  }
  .app-header {
    position: absolute; left: 0; top: 0; width: 100%; height: 135px;
    background: var(--brand-green);
    color: #fff;
  }
  .brand-name {
    position: absolute; left: 23px; top: 48px;
    font-size: 38px; font-weight: 500; letter-spacing: 0.5px;
  }
  .header-action {
    position: absolute; left: 386px; top: 51px;
    display: flex; align-items: center; gap: 11px;
    font-size: 18.5px; font-weight: 600; letter-spacing: 0.3px;
  }
  .section-title {
    position: absolute; left: 52px; top: 158px;
    font-size: 18.5px; font-weight: 500; color: var(--text-dark);
  }
  .field {
    position: absolute; left: 52px; width: 553px; height: 42px;
    background: var(--field-bg);
    padding: 10px 14px 0;
    font-size: 18px; font-weight: 300; color: var(--placeholder);
  }
  .field--textarea { height: 92px; }
  .field--select svg { position: absolute; right: 21px; top: 16px; }
  .logo-row { position: absolute; left: 0; top: 790px; width: 100%; height: 62px; }
  .logo-label {
    position: absolute; left: 66px; top: 20px;
    font-size: 18.5px; font-weight: 400; color: var(--label-grey);
  }
  .logo-preview {
    position: absolute; left: 140px; top: 2px; width: 62px; height: 58px;
    background: var(--field-bg);
  }
  .upload-button {
    position: absolute; left: 219px; top: 16px; width: 121px; height: 31px;
    background: var(--field-bg);
    font-size: 14.5px; color: var(--text-dark);
    display: flex; align-items: center; justify-content: center;
  }
  .upload-hint {
    position: absolute; left: 361px; top: 23px;
    font-size: 14.3px; color: var(--text-dark);
  }
  .save-button {
    position: absolute; left: 56px; top: 1076px; width: 540px; height: 57px;
    border: 1.5px solid var(--brand-green); border-radius: 29px;
    display: flex; align-items: center; justify-content: center;
    font-size: 22px; font-weight: 500; color: var(--brand-green);
  }
</style>
</head>
<body>
  <main class="app-screen">
    <header class="app-header">
      <div class="brand-name">Quillmoray</div>
      <div class="header-action">
        <svg width="40" height="40" viewBox="0 0 40 40" aria-hidden="true">
          <circle cx="20" cy="20" r="18" fill="none" stroke="#fff" stroke-width="2.2"/>
          <circle cx="20" cy="12" r="2.4" fill="#fff"/>
          <rect x="18" y="17" width="4" height="13" fill="#fff"/>
          <rect x="15.5" y="28" width="9" height="2.5" fill="#fff"/>
          <rect x="15.5" y="17" width="4" height="2.3" fill="#fff"/>
        </svg>
        <span>ADD/EDIT BUSINESS</span>
      </div>
    </header>

    <h2 class="section-title">Basic Information</h2>

    <div class="field" style="top:198px">Business Name</div>
    <div class="field field--select" style="top:258px">Business Category
      <svg width="14" height="12" viewBox="0 0 14 12" aria-hidden="true"><path d="M0 0H14L7 12Z" fill="var(--arrow-grey)"/></svg>
    </div>
    <div class="field field--textarea" style="top:321px">Business Description</div>
    <div class="field" style="top:432px">Services</div>
    <div class="field" style="top:490px">Address</div>
    <div class="field" style="top:548px">Business Phone</div>
    <div class="field" style="top:606px">Business Email</div>
    <div class="field" style="top:661px">Business Website</div>
    <div class="field" style="top:716px">Keywords</div>

    <div class="logo-row">
      <span class="logo-label">Logo</span>
      <div class="logo-preview" role="img" aria-label="Business logo preview placeholder"></div>
      <div class="upload-button">Upload File</div>
      <span class="upload-hint">upload only jpg,jpeg,gif,png,bmp</span>
    </div>

    <div class="field" style="top:891px">Contact Person</div>
    <div class="field" style="top:944px">Email</div>
    <div class="field field--select" style="top:996px">Business Role
      <svg width="14" height="12" viewBox="0 0 14 12" aria-hidden="true"><path d="M0 0H14L7 12Z" fill="var(--arrow-grey)"/></svg>
    </div>

    <div class="save-button">Save and Next</div>
  </main>
</body>
</html>
```